Flyer for local business that installs fences and sells fence materials

We recently began selling fence materials, in addition to also doing fence installations. We need a flyer that displays our business information and photos of our work, as well as a flyer that shows customers they have the option to buy materials only also.

If they are looking to build a fence - we can help by installing it, or if they want to install themselves, they can buy the materials only from us too. We provide a lifetime warranty on all materials and installations. More information about the company is here: www.BrambleRailWorks.com

Its important to have the company logo, phone number, email and business hours listed (Monday - Thursday 9AM - 3PM, Friday 9AM - 1PM).

It is also important to show the fence material types we offer:
Wood, Chainlink, Vinyl and Aluminum
Updates

Updated with more photos and url to website www.bramblerailworks.com for details

Target Market(s)

Residential Homeowners

Industry/Entity Type

Construction

Font styles to use
Sans Serif
Other font styles liked:
• Arial

Colors
0054AA
0677BA
7BADD7
CADEEF
E8F1F8

Requirements
Must have
• Photos of the fencing we offer
Nice to have
• A way to explain to customers they can hire us to install, or just buy the materials from us
Should not have
• Too many colors or too many words

```html
<!DOCTYPE html>
<html lang="en">
<head>
<meta charset="utf-8">
<title>Bramble Rail Works Flyer</title>
<link href="https://fonts.googleapis.com/css2?family=Montserrat:wght@300;400;500;600;700;800;900&display=swap" rel="stylesheet">
<style>
:root{
  --page-bg:#e4e4e4;
  --paper:#ffffff;
  --brand-blue:#3d86c6;
  --deep-blue:#2f7cc0;
  --brown:#5b3a22;
  --text-dark:#2a2a2a;
  --orange:#e8912c;
  --orange-dark:#d07a1c;
  --rule:#9a9a9a;
}
*{margin:0;padding:0;box-sizing:border-box}
html,body{width:1200px;height:2865px;overflow:hidden;background:var(--page-bg)}
body{position:relative;font-family:"Montserrat",Arial,sans-serif}
.flyer{
  position:absolute;left:50px;top:721px;width:806px;height:1043px;
  transform:scale(1.3648);transform-origin:0 0;
  background:var(--paper);overflow:hidden;
  box-shadow:0 6px 20px rgba(0,0,0,.18);
}
.flyer-art{position:absolute;left:0;top:0}
.t{position:absolute;white-space:nowrap;line-height:1}
.brand-name{left:88px;top:68px;font-size:29px;font-weight:800;color:var(--brand-blue);letter-spacing:.3px}
.brand-mark{position:absolute;left:56px;top:74px;width:22px;height:22px;border-radius:50%;background:var(--orange)}
.brand-phone{left:88px;top:104px;font-size:29px;font-weight:800;color:var(--text-dark)}
.brand-tagline{left:88px;top:141px;font-size:9.5px;font-weight:700;color:var(--text-dark)}

.hero-text{position:absolute;left:66px;top:410px;width:314px;text-align:center;color:#fff;line-height:1}
.hero-text .light{display:block;font-size:22px;font-weight:400;margin-bottom:3px}
.hero-text .bold{display:block;font-size:27px;font-weight:800;margin-bottom:1px}

.perks{position:absolute;left:85px;top:622px;width:226px;list-style:none}
.perks li{height:32.8px;border-bottom:1px solid var(--rule);font-size:12.2px;font-weight:600;color:var(--brown);display:flex;align-items:center;gap:4px;padding-top:1px}
.perks li:last-child{border-bottom:none;flex-wrap:wrap;align-content:center}
.perks svg{flex:none}
.perks .note{display:block;width:100%;padding-left:15px;font-size:10px;font-weight:400;color:#555;margin-top:1px}

.steps-title{position:absolute;left:83px;top:908px;font-size:24px;font-weight:800;color:var(--brown);line-height:.95}
.steps{position:absolute;color:#fff;font-size:11.5px;font-weight:600}
.step-1{left:85px;top:980px}.step-2{left:85px;top:1002px}
.step-3{left:271px;top:979px}.step-4{left:271px;top:1002px}

.estimate{position:absolute;left:349px;top:642px;width:200px;color:#fff}
.estimate h2{font-size:24px;font-weight:800;line-height:.92;margin-bottom:8px}
.estimate p{font-size:12.5px;font-weight:500;line-height:1}
.estimate p + p{margin-top:10px;font-size:13.5px;font-weight:600}

.materials-head{position:absolute;left:573px;top:645px;color:#fff;font-size:18px;font-weight:800;line-height:.95}
.material{position:absolute;left:636px;color:#fff;font-size:15.5px;font-weight:800}

.contact-label{position:absolute;left:477px;top:955px;font-size:14px;font-weight:700;color:var(--text-dark)}
.contact-phone{position:absolute;left:477px;top:978px;font-size:19px;font-weight:800;color:#fff}
.contact-web{position:absolute;left:477px;top:1001px;font-size:9.5px;font-weight:700;color:#fff}
</style>
</head>
<body>
<main class="flyer">
  <svg class="flyer-art" width="806" height="1043" viewBox="0 0 806 1043">
    <defs>
      <linearGradient id="photoTone" x1="0" y1="0" x2="1" y2="1">
        <stop offset="0" stop-color="#4d5a34"/>
        <stop offset=".45" stop-color="#c9a877"/>
        <stop offset=".75" stop-color="#e0c79c"/>
        <stop offset="1" stop-color="#6e7a45"/>
      </linearGradient>
      <linearGradient id="woodTone" x1="0" y1="0" x2="1" y2="1">
        <stop offset="0" stop-color="#ec9a38"/>
        <stop offset="1" stop-color="var(--orange-dark)"/>
      </linearGradient>
      <linearGradient id="vinylTone" x1="0" y1="0" x2="0" y2="1">
        <stop offset="0" stop-color="#3f7fd0"/>
        <stop offset=".45" stop-color="#f2f2f2"/>
        <stop offset="1" stop-color="#8a7350"/>
      </linearGradient>
      <linearGradient id="chainTone" x1="0" y1="0" x2="1" y2="1">
        <stop offset="0" stop-color="#9fb38a"/>
        <stop offset="1" stop-color="#c8ccc4"/>
      </linearGradient>
    </defs>

    <!-- main installation photo area -->
    <path role="img" aria-label="Photo of an installer fitting a new wooden privacy fence in a grassy yard"
      d="M0,0 H806 V205 C770,370 650,520 470,585 C330,630 150,600 0,560 Z" fill="url(#photoTone)"/>
    <!-- white header blob -->
    <path d="M0,0 H571 C520,120 400,215 230,218 C130,220 50,190 0,165 Z" fill="var(--paper)"/>
    <!-- orange accent arc -->
    <path d="M806,225 C770,390 660,520 520,590" stroke="var(--orange)" stroke-width="11" fill="none"/>
    <!-- orange wood panel -->
    <path role="img" aria-label="Warm orange wood grain panel" d="M806,433 C700,470 615,560 592,643 L563,643 V1043 H806 Z" fill="url(#woodTone)"/>

    <!-- small photo circles -->
    <circle cx="681" cy="465" r="73" fill="#fff"/>
    <circle role="img" aria-label="Photo of a chainlink fence" cx="681" cy="465" r="66" fill="url(#chainTone)"/>

    <!-- brown estimate box -->
    <path d="M326,560 H563 V873 Q563,913 523,913 H366 Q326,913 326,873 Z" fill="var(--brown)"/>

    <circle cx="526" cy="508" r="112" fill="#fff"/>
    <circle role="img" aria-label="Photo of a white vinyl privacy fence beside new homes" cx="526" cy="508" r="104" fill="url(#vinylTone)"/>

    <!-- hero circle -->
    <circle cx="223" cy="458" r="157" fill="var(--brand-blue)"/>

    <!-- materials header band -->
    <rect x="563" y="643" width="243" height="45" fill="var(--deep-blue)"/>

    <!-- material icons and rules -->
    <g fill="#fff" stroke="var(--brown)" stroke-width="2">
      <circle cx="606" cy="728" r="20"/>
      <circle cx="606" cy="786" r="20"/>
      <circle cx="606" cy="843" r="20"/>
      <circle cx="611" cy="900" r="20"/>
    </g>
    <g stroke="var(--brown)" stroke-width="2" fill="none" stroke-linecap="round">
      <path d="M597,736 V722 M603,736 V718 M609,736 V720 M615,736 V724 M594,726 H618"/>
      <path d="M598,794 L614,778 M601,784 a4,4 0 1 1 6,-6 M611,788 a4,4 0 1 1 -6,6"/>
      <path d="M596,852 V838 l3,-3 3,3 V852 M604,852 V838 l3,-3 3,3 V852 M612,852 V838 l3,-3 3,3 V852 M594,842 H620 M594,848 H620"/>
      <path d="M600,910 V892 M622,910 V892 M600,895 H622 M600,907 H622 M605,895 V907 M610,895 V907 M615,895 V907"/>
    </g>
    <g stroke="#fff" stroke-width="1.2">
      <line x1="631" y1="757" x2="731" y2="757"/>
      <line x1="631" y1="814" x2="731" y2="814"/>
      <line x1="631" y1="871" x2="731" y2="871"/>
      <line x1="631" y1="928" x2="731" y2="928"/>
    </g>

    <!-- steps band -->
    <path d="M0,966 H430 A31,31 0 0 1 430,1028 H0 Z" fill="var(--brown)"/>
    <!-- contact band -->
    <path d="M453,971 H668 L690,1018 H460 Q453,1018 453,1011 Z" fill="var(--deep-blue)"/>
  </svg>

  <span class="brand-mark"></span>
  <span class="t brand-name">Bramble Rail Works</span>
  <span class="t brand-phone">704-555-0142</span>
  <span class="t brand-tagline">"Because Good Fences Make Good Neighbors"</span>

  <div class="hero-text">
    <span class="light">SELLING</span>
    <span class="light">FENCE MATERIALS,</span>
    <span class="bold">IN ADDITION</span>
    <span class="bold">DOING FENCE</span>
    <span class="bold">INSTALLATIONS.</span>
  </div>

  <ul class="perks">
    <li><svg width="11" height="11" viewBox="0 0 12 12"><circle cx="6" cy="6" r="5" fill="none" stroke="currentColor" stroke-width="1.4"/><path d="M3.5,6 L5.5,8 L9,4" fill="none" stroke="currentColor" stroke-width="1.4"/></svg>Free Estimates</li>
    <li><svg width="11" height="11" viewBox="0 0 12 12"><circle cx="6" cy="6" r="5" fill="none" stroke="currentColor" stroke-width="1.4"/><path d="M3.5,6 L5.5,8 L9,4" fill="none" stroke="currentColor" stroke-width="1.4"/></svg>Professional Installation</li>
    <li><svg width="11" height="11" viewBox="0 0 12 12"><circle cx="6" cy="6" r="5" fill="none" stroke="currentColor" stroke-width="1.4"/><path d="M3.5,6 L5.5,8 L9,4" fill="none" stroke="currentColor" stroke-width="1.4"/></svg>Concrete in EVERY Post</li>
    <li><svg width="11" height="11" viewBox="0 0 12 12"><circle cx="6" cy="6" r="5" fill="none" stroke="currentColor" stroke-width="1.4"/><path d="M3.5,6 L5.5,8 L9,4" fill="none" stroke="currentColor" stroke-width="1.4"/></svg>HOA Submission Assistance</li>
    <li><svg width="11" height="11" viewBox="0 0 12 12"><circle cx="6" cy="6" r="5" fill="none" stroke="currentColor" stroke-width="1.4"/><path d="M3.5,6 L5.5,8 L9,4" fill="none" stroke="currentColor" stroke-width="1.4"/></svg>Lifetime Workmanship Warranty</li>
    <li><svg width="11" height="11" viewBox="0 0 12 12"><circle cx="6" cy="6" r="5" fill="none" stroke="currentColor" stroke-width="1.4"/><path d="M3.5,6 L5.5,8 L9,4" fill="none" stroke="currentColor" stroke-width="1.4"/></svg>Experienced Installation Teams</li>
    <li><svg width="11" height="11" viewBox="0 0 12 12"><circle cx="6" cy="6" r="5" fill="none" stroke="currentColor" stroke-width="1.4"/><path d="M3.5,6 L5.5,8 L9,4" fill="none" stroke="currentColor" stroke-width="1.4"/></svg>Quality Workmanship &amp; Materials</li>
    <li><svg width="11" height="11" viewBox="0 0 12 12"><circle cx="6" cy="6" r="5" fill="none" stroke="currentColor" stroke-width="1.4"/><path d="M3.5,6 L5.5,8 L9,4" fill="none" stroke="currentColor" stroke-width="1.4"/></svg>FREE Gate Adjustments for LIFE<span class="note">*some restrictions apply</span></li>
  </ul>

  <div class="steps-title">STEPS TO A NEW<br>FENCE INSTALLATION</div>
  <span class="steps step-1">1 GETTING A FREE ESTIMATE</span>
  <span class="steps step-2">2 HOA APPROVALS</span>
  <span class="steps step-3">3 UNDERGROUND UTILITIES</span>
  <span class="steps step-4">4 WARRANTY</span>

  <section class="estimate">
    <h2>ESTIMATES<br>ARE ALWAYS<br>FREE</h2>
    <p>Call, email, or message us online to schedule an in-person estimate. If you know your measurements OR have a lot survey, email or call us for a virtual estimate! Monday -Thurs 9AM - 3PM, Friday 9AM - 1 PM</p>
    <p>Beautiful, professionally installed fences at affordable prices! Many fence styles available.</p>
  </section>

  <div class="materials-head">MATERIAL<br>TYPES WE OFFER:</div>
  <span class="t material" style="top:720px">WOOD</span>
  <span class="t material" style="top:778px">CHAINLINK</span>
  <span class="t material" style="top:835px">VINYL</span>
  <span class="t material" style="top:892px">Aluminum</span>

  <span class="t contact-label">Contact Us Now!!</span>
  <span class="t contact-phone">704-555-0142</span>
  <span class="t contact-web">www.bramblerailworks.com</span>
</main>
</body>
</html>
```